Zielgruppe
Regionale Kooperation der KELV Generalvertretung bei Baufinanzierungen
Beste Kondition für ihre private Immobilienfinanzierung im Raum Südostbayern
Aufgabenstellung
Es soll ein Misch aus Bild und Text sein. Die 4 wichtigen Säulen sollten herausgehoben werden mit Text und Bild
1) Unverbindliche und verständliche Beratung (z.B Vektorgrafi mit einer Waage mit % Zeichen in den Schalen)
2) Es entstehen keine Extrakosten (z.B. eine Vektorgrafik mit Münzen)
3) Gemeinsam von der Angebotsphase bis zum Einzug (z.B. schüttelnde Hände)
4) Wir machen deine Bankenrunde (z.B. Haus mit % Zeichen)
Es soll am Ende ein Roll-Up Banner Design sein. Die Nähe zum Kunden soll und ist hier der entscheidende Faktor.

```html
<!DOCTYPE html>
<html lang="de">
<head>
<meta charset="utf-8">
<title>Roll-Up – Regionale Kooperation</title>
<link href="https://fonts.googleapis.com/css2?family=Poppins:wght@600;700;800&display=swap" rel="stylesheet">
<style>
  :root {
    --blue: #27368c;
    --blue-dark: #1d2a73;
    --blue-light: #3b4ea6;
    --red: #d42027;
    --red-dark: #a8161c;
    --yellow: #fff200;
    --gold: #e8b21a;
    --silver: #c9cbd1;
    --white: #ffffff;
    --paper: #f6f6f6;
    --grey-line: #d8d8d8;
    --stage: #ecebea;
  }
  * { box-sizing: border-box; margin: 0; padding: 0; }
  html, body { width: 1200px; height: 1117px; overflow: hidden; background: var(--stage); }
  body { font-family: "Poppins", sans-serif; position: relative; }

  .rollup {
    position: absolute;
    left: 390px; top: 28px;
    width: 610px; height: 1540px;
    transform: scale(0.689);
    transform-origin: top left;
    background: var(--paper);
    overflow: hidden;
    box-shadow: 0 6px 24px rgba(0,0,0,.18);
  }
  .band-top {
    position: absolute; left: 0; top: 0; width: 100%; height: 600px;
    background: radial-gradient(ellipse at 60% 0%, #3a56c4 0%, var(--blue) 55%, var(--blue-dark) 100%);
  }
  .band-bottom {
    position: absolute; left: 0; top: 1030px; width: 100%; height: 400px;
    background: var(--red);
  }
  .band-bottom-edge {
    position: absolute; left: 0; top: 1422px; width: 100%; height: 36px;
    background: var(--red-dark);
  }
  .headline {
    position: absolute; top: 84px; width: 100%; text-align: center;
    font-weight: 800; line-height: 1; text-transform: uppercase;
  }
  .headline .line-1 { display: block; color: var(--white); font-size: 60px; letter-spacing: 1px; }
  .headline .line-2 { display: block; color: var(--yellow); font-size: 64px; margin-top: 2px; }

  .subline {
    position: absolute; left: 42px; top: 224px; width: 526px; height: 96px;
    border: 2px solid var(--white); border-radius: 12px;
    display: flex; align-items: center; justify-content: center; text-align: center;
    color: var(--white); font-weight: 700; font-size: 27px; line-height: 1.2; text-transform: uppercase;
  }

  .pillar {
    position: absolute; width: 266px; height: 384px;
    background: var(--white); border-radius: 22px;
    box-shadow: 0 4px 10px rgba(0,0,0,.18);
    overflow: hidden;
  }
  .pillar.p1 { left: 28px; top: 378px; }
  .pillar.p2 { left: 316px; top: 378px; }
  .pillar.p3 { left: 28px; top: 788px; }
  .pillar.p4 { left: 316px; top: 788px; }

  .pillar-visual {
    position: absolute; left: 0; top: 0; width: 100%; height: 278px;
    background: linear-gradient(180deg, #fbfbfb 0%, #f1f1f2 100%);
  }
  .pillar-visual::after {
    content: ""; position: absolute; left: 50%; top: 50%;
    width: 170px; height: 170px; margin: -92px 0 0 -85px;
    border-radius: 24px;
  }
  .pillar-visual::before {
    content: ""; position: absolute; left: 50%; bottom: 28px;
    width: 170px; height: 18px; margin-left: -85px;
    border-radius: 50%; background: rgba(0,0,0,.08);
  }
  .visual-rate::after { background: linear-gradient(160deg, #e4e5e9 0%, var(--silver) 50%, #e24a50 100%); }
  .visual-coins::after { background: linear-gradient(160deg, #ffd84a 0%, var(--gold) 60%, #c48e0c 100%); border-radius: 50%; }
  .visual-hands::after { background: linear-gradient(135deg, #e5343a 0%, var(--red) 50%, var(--blue-light) 100%); border-radius: 50% 50% 24px 24px; }
  .visual-house::after { background: linear-gradient(160deg, #ef4a50 0%, var(--red) 60%, #a8161c 100%); }

  .pillar-caption {
    position: absolute; left: 6px; right: 6px; bottom: 6px; height: 100px;
    background: linear-gradient(160deg, var(--blue) 70%, var(--blue-light) 100%);
    border-radius: 0 0 18px 18px;
    display: flex; align-items: center; justify-content: center; text-align: center;
    color: var(--white); font-weight: 700; font-size: 18px; line-height: 1.12;
  }

  .claim {
    position: absolute; top: 1200px; width: 100%; text-align: center;
    color: var(--white); font-weight: 800; font-size: 32px; line-height: 1.15; text-transform: uppercase;
  }

  .web-tab {
    position: absolute; left: 108px; top: 1398px; width: 395px; height: 80px;
    background: var(--paper); border-radius: 30px 30px 0 0;
  }
  .web-address {
    position: absolute; top: 1424px; width: 100%; text-align: center;
    color: var(--blue); font-weight: 800; font-size: 30px;
  }
  .foot-rule {
    position: absolute; left: 38px; top: 1492px; width: 532px; height: 4px;
    background: var(--grey-line); border-radius: 2px;
  }
</style>
</head>
<body>
  <main class="rollup">
    <div class="band-top"></div>
    <div class="band-bottom"></div>
    <div class="band-bottom-edge"></div>

    <h1 class="headline">
      <span class="line-1">Regionale</span>
      <span class="line-2">Kooperation</span>
    </h1>

    <div class="subline">Er KELV Generalverterung<br>bei Baufinanzierungen</div>

    <section class="pillar p1">
      <div class="pillar-visual visual-rate" role="img" aria-label="Silberne Servierglocke mit rotem Prozentzeichen"></div>
      <p class="pillar-caption">Unverbindliche<br>und verständliche<br>Beratung</p>
    </section>
    <section class="pillar p2">
      <div class="pillar-visual visual-coins" role="img" aria-label="Stapel goldener Münzen"></div>
      <p class="pillar-caption">Es entstehen<br>keine<br>Extrakosten</p>
    </section>
    <section class="pillar p3">
      <div class="pillar-visual visual-hands" role="img" aria-label="Händedruck in Herzform, rot und blau"></div>
      <p class="pillar-caption">Gemeinsam von<br>der Angebotsphase<br>bis zum Einzug</p>
    </section>
    <section class="pillar p4">
      <div class="pillar-visual visual-house" role="img" aria-label="Rotes Haus mit weißem Prozentzeichen"></div>
      <p class="pillar-caption">Wir machen<br>deine<br>Bankenrunde</p>
    </section>

    <p class="claim">Beste Kondition<br>fur Ihreprivate<br>Immobilienfinanzierung<br>im Raum Sudostbayern</p>

    <div class="web-tab"></div>
    <p class="web-address">HIERWEBSITE.COM</p>
    <div class="foot-rule"></div>
  </main>
</body>
</html>
```